Panel Forge App redesign proposal

Proposal for redesign of the main screens of our comic book creation app Panel Forge which is currently available for iPhone and iPad on App Store here:

https://apps.quillmarket.example/us/app/panel-forge/id907214563?mt=8

We are looking for suggestions for a new modern, polished and professional look for Panel Forge. The focus should be on icons, colors, and fonts on the main editing screen.

This project is not a full redesign, but should merely contain suggestions for what the app could look like!

Proposals are preferably based on the current design/layout of the app's components, and should focus on redesign of icons or colors.

Proposals should be based on the screenshots on App Store (attached). I.e. preferably replacing them with the new look of the app. Proposals are required in both iPhone 6 and iPad (Air/Mini) screen sizes (Retina).

The new look should be:
• Professional and clean
• Stay somewhat in line with iOS guidelines
• Mostly flat design
• Quiet (not dominate users' content)
• Exciting but not too playful
• Accessible and easy to navigate (no ambiguous icons or gestures. Labels on tool buttons).
• Use only fonts on iOS7 or higher

Preferably, most or all 10 attached screenshots should be replaced with your proposed counterparts reusing the current user content ("Garden Goblin" and "On the hill") . I.e. replace fonts, colors, and icons only. You are free to create your own screenshots from scratch, if you feel that can better reflect your proposal.

We can provide free access to the app using promotional codes.

We are interested in redesigning the app, so if we see a good proposal we will be interested in further collaboration

About the app
------------------------------------------
Panel Forge is a comic book creation app for iOS (iPad and iPhone) purchased and downloaded by many hundreds of thousands of users.

The app has been around since 2009 with several major updates and is one of the first and best comic book creation apps for iOS.

It is a very feature rich app. Its features include:
• page design with many photos
• books with multiple pages
• many balloon options (head and tail settings)
• merge of balloons and adding tail control points for better tail control
• complex text layout (warp and perspective)
• easy in-app font installation from font websites
• stickers (built-in and ability to add)
• built-in drawing
• image filters
• image blending modes and opacity
• built-in Dropbox file support
• PDF support (both import and export)
• layer management
and much, much more.

Please contact us if you would like promotional code to test the app.
Updates

Reason: Haven't received satisfactory suggestions. At least a number of both iPhone and iPad screenshots are needed.

Target Market(s)

Children, parents, and hobby comic book creators.

Requirements
Must have
• Replace at least 6 screenshots with your own proposal.
Nice to have
• • Professional, clean, simple
• • Stay somewhat in line with iOS guidelines
• • Mostly flat design
• • Quiet (not dominate users' content)
• • Accessible and easy to navigate (no ambiguous icons or gestures)
Should not have
• • Not too many items on screen
• • Not ambiguous
• • Not too colorful/playful

```html
<!DOCTYPE html>
<html lang="en">
<head>
<meta charset="utf-8">
<title>Panel Forge – Bubbles editor</title>
<link rel="stylesheet" href="https://fonts.googleapis.com/css2?family=Bangers&family=Roboto+Condensed:wght@500;700&family=Patrick+Hand&display=swap">
<style>
  :root{
    --stage:#000000;
    --chrome:#3d3c3e;
    --rail:#4a4a4c;
    --tile:#e8e8e9;
    --label-band:#3f3f41;
    --accent:#45a78d;
    --ink:#1d1d1d;
    --paper:#ffffff;
    --title-top:#ff8a1f;
    --title-bottom:#e8322a;
    --handle:#f07b1a;
  }
  *{box-sizing:border-box;margin:0;padding:0}
  html,body{width:1200px;height:1200px;overflow:hidden;background:var(--stage)}
  .canvas{position:relative;width:1200px;height:1200px}
  .screen{position:absolute;left:35px;top:241px;width:1132px;height:720px;background:var(--paper);overflow:hidden}

  .title-band{position:absolute;left:0;top:0;width:926px;height:168px;background:var(--chrome);display:flex;align-items:center;justify-content:center}
  .comic-title{font-family:'Bangers',cursive;font-weight:400;font-size:82px;letter-spacing:1px;transform:skewX(-6deg);
    background:linear-gradient(180deg,var(--title-top),var(--title-bottom));-webkit-background-clip:text;background-clip:text;color:transparent;padding-right:10px}

  .panel{position:absolute;overflow:hidden}
  .panel-kitchen{left:0;top:181px;width:458px;height:264px;background:radial-gradient(circle at 60% 50%,#e9b59a 0,#c46b36 35%,#8a3d16 100%)}
  .panel-house{left:469px;top:181px;width:457px;height:264px;background:linear-gradient(180deg,#2f95d8 0%,#8cc6ec 38%,#b9aa96 55%,#8a7a66 78%,#5f8a3b 92%,#4a6b2c 100%)}
  .panel-portrait{left:0;top:456px;width:926px;height:264px;background:radial-gradient(ellipse at 52% 55%,#d8b8a4 0,#8a5e3e 28%,#4a3224 60%,#3a2a20 100%)}

  .rail{position:absolute;left:926px;top:0;width:102px;height:720px;background:var(--rail)}
  .tools{position:absolute;left:1028px;top:0;width:104px;height:720px;background:var(--tile)}
  .tool{position:absolute;left:0;width:104px;display:flex;align-items:center;justify-content:center}
  .tool-label{position:absolute;left:0;width:104px;background:var(--label-band);color:#fff;font-family:'Roboto Condensed',sans-serif;font-weight:700;font-size:15px;display:flex;align-items:center;justify-content:center;letter-spacing:.2px}
  .tool.is-active{background:var(--accent)}
  .effect-word{font-family:'Bangers',cursive;font-size:36px;color:#3a3a3a;letter-spacing:1px}
  .done-label{font-family:'Roboto Condensed',sans-serif;font-weight:500;font-size:16px;color:#2d2d2d;margin-top:6px}

  .bubble-text{position:absolute;text-align:center;color:var(--ink);font-family:'Patrick Hand',cursive;white-space:nowrap}
  .bubble-round{left:33px;top:236px;width:100px;font-size:18px;line-height:20px;text-transform:uppercase;transform:rotate(-3deg)}
  .bubble-box{left:70px;top:538px;width:168px;font-size:31px;line-height:32px}
  .burst-text{position:absolute;left:599px;top:288px;width:180px;text-align:center;font-family:'Bangers',cursive;font-size:44px;line-height:44px;color:#222;letter-spacing:1px;transform:skewX(-8deg)}

  .hint{position:absolute;left:541px;top:638px;width:385px;height:48px}
  .hint-text{position:absolute;left:72px;top:0;height:48px;display:flex;align-items:center;font-family:'Roboto Condensed',sans-serif;font-weight:500;font-size:21px;color:#fff;letter-spacing:.2px}
  svg.layer{position:absolute;left:0;top:0}
</style>
</head>
<body>
<div class="canvas">
  <div class="screen">
    <header class="title-band"><h1 class="comic-title">GARDEN GOBLIN</h1></header>

    <div class="panel panel-kitchen" role="img" aria-label="Photo of a little girl cooking over a steaming pot in a wooden kitchen"></div>
    <div class="panel panel-house" role="img" aria-label="Photo of a suburban house with a porch under a sunny blue sky"></div>
    <div class="panel panel-portrait" role="img" aria-label="Photo of a smiling curly-haired toddler"></div>

    <div class="rail"></div>

    <svg class="layer" width="1132" height="720" viewBox="0 0 1132 720" aria-hidden="true">
      <ellipse cx="83" cy="271" rx="60" ry="58" fill="#fff"/>
      <polygon points="118,305 167,329 100,326" fill="#fff"/>
      <circle cx="167" cy="329" r="5" fill="var(--handle)"/>
      <path d="M126 209 q14 0 17 14 m-5 -3 l5 4 l4 -5" fill="none" stroke="var(--accent)" stroke-width="3" stroke-linecap="round"/>
      <path d="M30 319 q0 13 16 15 m-3 -5 l4 5 l-5 3" fill="none" stroke="var(--accent)" stroke-width="3" stroke-linecap="round"/>

      <polygon points="627,286 567,318 625,335 600,361 676,355 680,385 731,365 784,372 790,345 810,340 812,325 800,311 818,288 778,284 775,255 740,272 705,251 690,272 660,260 657,282" fill="#fff"/>

      <rect x="70" y="523" width="168" height="122" fill="#fff"/>
      <polygon points="237,572 361,568 237,610" fill="#fff"/>
      <circle cx="361" cy="568" r="5" fill="var(--handle)"/>

      <polygon points="977,28 967,36 987,36" fill="#e5e5e5"/>
      <polygon points="977,694 967,686 987,686" fill="#e5e5e5"/>
      <path d="M960 121 h34 v30 h-23 l-8 13 v-13 h-3 z" fill="var(--accent)"/>
      <path d="M966 251 h23 a6 6 0 0 1 6 6 v18 a6 6 0 0 1 -6 6 h-7 l-9 13 v-13 h-7 a6 6 0 0 1 -6 -6 v-18 a6 6 0 0 1 6 -6 z" fill="var(--accent)"/>
      <path d="M977 381 a17 16 0 1 1 -2 31 l-5 12 l-2 -14 a17 16 0 0 1 9 -29 z" fill="var(--accent)"/>
      <path d="M966 513 h27 v18 a10 10 0 0 1 -10 10 l-10 14 v-14 h-7 a6 6 0 0 1 -6 -6 v-16 a6 6 0 0 1 6 -6 z" fill="var(--accent)"/>
      <polygon points="1012,523 1028,509 1028,537" fill="var(--accent)"/>
    </svg>

    <div class="bubble-text bubble-round">This is<br>going to<br>be great !</div>
    <div class="burst-text">BOOOOM</div>
    <div class="bubble-text bubble-box">She is<br>Awesome<br>:D</div>

    <div class="hint">
      <svg class="layer" width="385" height="48" viewBox="0 0 385 48" aria-hidden="true">
        <polygon points="0,24 24,0 385,0 385,48 24,48" fill="var(--accent)"/>
        <g fill="#fff"><polygon points="42,10 37,16 47,16"/><polygon points="42,38 37,32 47,32"/><polygon points="28,24 34,19 34,29"/><polygon points="56,24 50,19 50,29"/></g>
      </svg>
      <div class="hint-text">DRAG A BALLON ON THE COMIC</div>
    </div>

    <nav class="tools">
      <div class="tool" style="top:0;height:187px">
        <svg width="52" height="52" viewBox="0 0 52 52" aria-hidden="true"><rect x="6" y="6" width="40" height="40" fill="none" stroke="#3a3a3a" stroke-width="5"/><g fill="#3a3a3a"><circle cx="6" cy="6" r="6"/><circle cx="46" cy="6" r="6"/><circle cx="6" cy="46" r="6"/><circle cx="46" cy="46" r="6"/></g></svg>
      </div>
      <div class="tool-label" style="top:187px;height:26px">SCALE</div>
      <div class="tool" style="top:213px;height:104px"><span class="effect-word">EFFECT</span></div>
      <div class="tool-label" style="top:317px;height:26px">EFFECTS</div>
      <div class="tool" style="top:343px;height:104px">
        <svg width="56" height="56" viewBox="0 0 56 56" aria-hidden="true"><polygon points="28,2 33,14 45,6 42,19 55,20 45,28 55,36 42,37 45,50 33,42 28,54 23,42 11,50 14,37 1,36 11,28 1,20 14,19 11,6 23,14" fill="#3a3a3a"/><text x="28" y="33" text-anchor="middle" font-family="Roboto Condensed, sans-serif" font-size="14" font-weight="700" fill="#fff">POW</text></svg>
      </div>
      <div class="tool-label" style="top:447px;height:26px">STICKERS</div>
      <div class="tool is-active" style="top:473px;height:104px">
        <svg width="48" height="52" viewBox="0 0 48 52" aria-hidden="true"><path d="M24 3 a21 20 0 1 1 -3 40 l-6 9 l0 -11 a21 20 0 0 1 9 -38 z" fill="#fff"/></svg>
      </div>
      <div class="tool-label" style="top:577px;height:27px">BUBBLES</div>
      <div class="tool" style="top:604px;height:116px;flex-direction:column">
        <svg width="52" height="40" viewBox="0 0 52 40" aria-hidden="true"><path d="M4 20 L18 34 L48 4" fill="none" stroke="#3a3a3a" stroke-width="6"/></svg>
        <span class="done-label">DONE</span>
      </div>
    </nav>
  </div>
</div>
</body>
</html>
```